Design a compelling Tarnwell Business Card that will drive people to my site

I want a business card that I can give to people—less to tell them who I am and more to direct them to my website. My website is a portal for Crestlane Aquatics Officials and a place for people who want to become Crestlane Aquatics Officials.
I am uploading my official company logo as well as a business card mockup that I did on my own. Please feel free to completely stray from this design.
I've included a screen recording of the homepage of my website as well.
Target Market(s)
Crestlane Aquatics Officials and people who desire to become one
Contact Information for Business Card
website url
Look and feel
Each slider illustrates characteristics of the customer's brand and the style your logo design should communicate.

```html
<!DOCTYPE html>
<html lang="en">
<head>
<meta charset="utf-8">
<title>Tarnwell Business Card</title>
<link href="https://fonts.googleapis.com/css2?family=Montserrat:wght@400;500;600;700&display=swap" rel="stylesheet">
<style>
  :root {
    --bg: #1d1e21;
    --navy: #2c4584;
    --slate: #7283a8;
    --paper: #d3d3d5;
    --ink: #2c4584;
    --muted: #7f8db4;
    --light: #e2e2e4;
    --rule: #c9b9c4;
  }
  * { margin: 0; padding: 0; box-sizing: border-box; }
  html, body { width: 1200px; height: 800px; overflow: hidden; }
  body {
    background: var(--bg);
    font-family: "Montserrat", sans-serif;
    position: relative;
  }
  .card {
    position: absolute;
    top: 251px;
    width: 520px;
    height: 298px;
    border-radius: 24px;
    overflow: hidden;
  }
  .card--front { left: 60px; background: var(--paper); }
  .card--back { left: 620px; background: var(--slate); }

  .front-wave { position: absolute; inset: 0; }
  .front-brand {
    position: absolute;
    left: 36px;
    top: 112px;
    display: flex;
    align-items: center;
    gap: 10px;
    color: var(--light);
    font-weight: 600;
    font-size: 32px;
    letter-spacing: -0.5px;
  }
  .brand-dot {
    width: 12px; height: 12px; border-radius: 50%;
    background: var(--light);
  }
  .contact {
    position: absolute;
    left: 300px;
    top: 130px;
    color: var(--ink);
  }
  .contact__name { font-weight: 700; font-size: 22px; letter-spacing: 0.2px; }
  .contact__role { font-weight: 500; font-size: 13px; color: var(--muted); margin-top: 3px; }
  .contact__rule { width: 34px; height: 2px; background: var(--ink); margin: 12px 0 10px; }
  .contact__line { font-weight: 500; font-size: 13px; line-height: 1.5; }

  .back-content {
    position: absolute;
    inset: 0;
    display: flex;
    flex-direction: column;
    align-items: center;
    justify-content: center;
  }
  .back-brand {
    color: var(--light);
    font-weight: 700;
    font-size: 58px;
    letter-spacing: -1px;
  }
  .back-rule { width: 130px; height: 2px; background: var(--rule); margin: 14px 0 12px; }
  .back-tagline {
    color: var(--light);
    font-weight: 500;
    font-size: 17px;
    letter-spacing: 0.4px;
  }
</style>
</head>
<body>
  <section class="card card--front">
    <svg class="front-wave" viewBox="0 0 520 298" preserveAspectRatio="none" aria-hidden="true">
      <path d="M0 0 H300 C290 90 250 150 225 190 C205 225 195 260 190 298 H0 Z" fill="var(--navy)"/>
    </svg>
    <div class="front-brand"><span class="brand-dot"></span>tarnwell</div>
    <div class="contact">
      <p class="contact__name">Marcus Leland</p>
      <p class="contact__role">CEO &amp; Founder</p>
      <div class="contact__rule"></div>
      <p class="contact__line">marcus@tarnwell.com</p>
      <p class="contact__line">(555) 210 - 4417</p>
    </div>
  </section>

  <section class="card card--back">
    <div class="back-content">
      <p class="back-brand">tarnwell.com</p>
      <div class="back-rule"></div>
      <p class="back-tagline">Where Pool Deck Officials Meet</p>
    </div>
  </section>
</body>
</html>
```